High end building company who specialise in architecturally designed homes needing a presentation do

We need a document/template that can be used in Indesign. We present proposal's, house plans, specifications at various stages throughout a building project from initial contact right through to completion. We want to have the same feel through out each presentation and be able to use the same first few pages and then be able to insert the contents. Sometimes the content will be A4 and other times when presenting plans will be A3. I have attached an example of one previously used for presenting plans (see 01_Conceptual) and one for proposals (see Proposal Example ). The document needs to have a minimalist look and feel very sophisticated to suit our client base. The look of the document should tie in with our logo design which is also attached.

```html
<!DOCTYPE html>
<html lang="en">
<head>
<meta charset="utf-8">
<title>Project Details</title>
<link href="https://fonts.googleapis.com/css2?family=Montserrat:wght@200;800&display=swap" rel="stylesheet">
<style>
  :root {
    --backdrop: #454344;
    --photo-light: #d4d4d4;
    --photo-mid: #9e9e9e;
    --photo-dark: #6c6c6c;
    --overlay-deep: #8e3a0e;
    --overlay-bright: #d4581c;
    --title-grey: #8c8c8c;
    --rule-light: #c9c9c9;
    --subtitle-white: #ffffff;
  }
  html, body {
    margin: 0;
    padding: 0;
    width: 1200px;
    height: 1200px;
    overflow: hidden;
    background: var(--backdrop);
  }
  .page {
    display: block;
    width: 1200px;
    height: 1200px;
  }
  .cover-title {
    font-family: "Montserrat", sans-serif;
    font-weight: 800;
    fill: var(--title-grey);
  }
  .cover-subtitle {
    font-family: "Montserrat", sans-serif;
    font-weight: 200;
    fill: var(--subtitle-white);
  }
</style>
</head>
<body>
<svg class="page" viewBox="0 0 1500 1500" xmlns="http://www.w3.org/2000/svg">
  <defs>
    <linearGradient id="facade-tone" x1="0" y1="0" x2="0" y2="1">
      <stop offset="0" stop-color="var(--photo-light)"/>
      <stop offset="0.5" stop-color="var(--photo-mid)"/>
      <stop offset="1" stop-color="var(--photo-light)"/>
    </linearGradient>
  </defs>

  <g class="cover-sheet">
    <rect class="cover-photo" x="77" y="250" width="1350" height="955" fill="url(#facade-tone)"
          role="img" aria-label="Black and white photograph of a timber-slatted house facade with a long glazed window reflecting hills"/>

    <rect class="overlay-window" x="157" y="445" width="1190" height="413" fill="var(--overlay-deep)" opacity="0.95"/>
    <rect class="overlay-band" x="157" y="858" width="1190" height="150" fill="var(--overlay-bright)" opacity="0.95"/>

    <line class="accent-rule" x1="357" y1="445" x2="727" y2="1008" stroke="var(--rule-light)" stroke-width="3"/>

    <text class="cover-title" x="585" y="557" font-size="76" textLength="713" lengthAdjust="spacingAndGlyphs">PROJECT DETAILS</text>
    <text class="cover-subtitle" x="200" y="965" font-size="32" textLength="362" lengthAdjust="spacingAndGlyphs">Halvorsen Residence</text>
  </g>
</svg>
</body>
</html>
```